Style Template created - Report Accounting and Advisory industry

We need a style template created to set out a report for advice. The report follows <br/><br/>- Cover Page - ( we would need to print to a letter head )<br/>- General Disclaimer<br/>- Space to add Excel Reports in to the document- Maybe inserted Pdf's later<br/>- Action Plan dot points under headings<br/>- List of Strategies to be adopted<br/><br/>Attached is a quick example word doc that needs Custom Style Templates made so that we can quickly format items added. Also the ugly PDF that we currently produce for clients <br/><br/>Red - is our preferred Colour<br/><br/>

Target Market(s)

Accounting / Business / Professionals

Industry/Entity Type

Accounting

Colors
ec1f27

Requirements
Nice to have
• Simple Clean design. Not to busy. Easy to modify the "wording text" in design
Should not have
• Too busy or too much color

```html
<!DOCTYPE html>
<html lang="en">
<head>
<meta charset="utf-8">
<title>Harlow Reed – Taxation Estimate Report Template</title>
<link href="https://fonts.googleapis.com/css2?family=Open+Sans:ital,wght@0,400;0,600;0,700;1,400&display=swap" rel="stylesheet">
<style>
  :root{
    --brand-red:#c8252c;
    --brand-red-band:#b5262d;
    --ink:#3a3a3a;
    --ink-soft:#5b5b5b;
    --rule:#444;
    --paper:#f7f7f7;
    --backdrop:#e2e2e2;
    --title-panel:#e9e9e9;
    --white:#ffffff;
  }
  *{box-sizing:border-box;margin:0;padding:0}
  html,body{width:1200px;height:900px;overflow:hidden}
  body{background:var(--backdrop);font-family:"Open Sans",Arial,sans-serif;color:var(--ink);position:relative}

  .page{position:absolute;background:var(--paper);overflow:hidden}
  .abs{position:absolute}

  /* brand name */
  .brand-name{font-family:"Open Sans",Arial,sans-serif;font-weight:600;color:var(--brand-red);letter-spacing:.5px;white-space:nowrap}
  .brand-tag{font-size:3.6px;color:#8a8a8a;letter-spacing:.4px;white-space:nowrap}
  .brand-dot{position:absolute;border-radius:50%;background:var(--brand-red)}

  /* running header */
  .run-rule{position:absolute;height:1px;background:var(--brand-red)}
  .run-title{position:absolute;font-size:2.6px;font-weight:700;color:#333;white-space:nowrap}

  .page-no{position:absolute;top:345px;width:22px;height:7px;background:var(--brand-red);color:var(--white);font-size:3.6px;line-height:7px;text-align:center}

  /* cover */
  .cover{left:186px;top:62px;width:265px;height:371px}
  .cover-band-top{left:0;top:0;width:100%;height:9px;background:var(--brand-red)}
  .cover-rule{left:15px;top:41px;width:193px;height:1px;background:var(--brand-red)}
  .client-name{left:30px;top:247px;font-size:6.6px;font-weight:700;color:#222}
  .client-rule{left:30px;top:256px;width:207px;height:.6px;background:#777}
  .report-title{left:30px;top:260px;font-size:5.6px;font-weight:600;color:#555}
  .report-date{left:30px;top:268px;font-size:5.6px;color:#555}
  .cover-footer{left:0;top:345px;width:100%;height:26px;background:var(--brand-red-band);color:var(--white);font-size:3px;font-weight:600;text-align:center;padding-top:7px;line-height:4.6px}

  /* disclaimer */
  .left-page{left:481px;top:62px;width:257px;height:372px}
  .right-page{left:739px;top:62px;width:255px;height:372px}
  .accent-bar{left:36px;top:61px;width:1.6px;height:232px;background:var(--brand-red)}
  .disclaimer{left:52px;top:70px;width:167px;font-size:4.3px;line-height:6.5px;color:var(--ink-soft)}
  .disclaimer h2{font-size:7.6px;font-weight:700;color:var(--brand-red);margin-bottom:3px;line-height:10px}
  .disclaimer p{margin-bottom:6.5px}
  .disclaimer h3{font-size:4.5px;font-weight:700;color:#333;line-height:6px}
  .sign-off{margin-top:18px;font-weight:700;color:#333;font-size:4.4px;line-height:5.6px}
  .insert-label{left:22px;top:33px;font-size:4.6px;font-style:italic;color:#444}

  /* action plan */
  .action-left{left:188px;top:467px;width:257px;height:372px}
  .action-right{left:445px;top:467px;width:259px;height:372px}
  .action-heading{position:absolute;left:25px;width:210px;font-size:4.1px;font-weight:600;color:#333;border-bottom:.7px solid var(--brand-red);padding-bottom:1px}
  .action-list{position:absolute;left:49px;top:55px;list-style:none;font-size:4.1px;font-style:italic;line-height:6.6px;color:#444}
  .action-list li::before{content:"";display:inline-block;width:1.8px;height:1.8px;border-radius:50%;background:var(--brand-red);margin:0 5px 0 -7px;vertical-align:middle}

  /* strategies */
  .title-panel{left:24px;top:33px;width:208px;height:20px;background:var(--title-panel)}
  .strategies-title{left:28px;top:33px;font-size:7.6px;font-weight:700;color:var(--brand-red)}
  .strategies-intro{left:28px;top:43px;font-size:3.6px;color:#555}
  .main-heading{left:28px;top:57px;font-size:5.6px;color:var(--brand-red)}
  .strategy-label{left:28px;top:65px;font-size:3.6px;color:#333}
  .strategies{left:28px;top:75px;width:205px}
  .strategy{margin-bottom:13px}
  .strategy h4{font-size:4.2px;font-weight:700;color:#222;border-bottom:.7px solid var(--rule);padding-bottom:.5px;margin-bottom:4px}
  .strategy p{font-size:2.9px;line-height:5.2px;color:#555;width:186px;margin-bottom:3px}
  .strategy ul{list-style:none;font-size:2.9px;line-height:6.8px;color:#555;padding-left:15px;margin-bottom:3px}
  .strategy ul.dash li::before{content:"–";margin:0 5px 0 -10px}
  .strategy ul.dot li{line-height:4.6px;margin-bottom:1.5px}
  .strategy ul.dot li::before{content:"•";margin:0 5px 0 -10px}
  .s1{margin-bottom:17px}

  /* back cover */
  .back-cover{left:739px;top:467px;width:260px;height:371px}
  .back-band{left:0;top:345px;width:100%;height:26px;background:var(--brand-red-band)}
</style>
</head>
<body>

<section class="page cover" aria-label="Cover page">
  <div class="abs cover-band-top"></div>
  <div class="abs" style="left:17px;top:15px">
    <div class="brand-name" style="font-size:12.5px">HARLOW REED</div>
    <div class="brand-tag">CHARTERED ACCOUNTANTS</div>
  </div>
  <div class="abs cover-rule"></div>
  <span class="brand-dot" style="left:219px;top:17px;width:31px;height:31px"></span>
  <div class="abs client-name">CLIENT NAME</div>
  <div class="abs client-rule"></div>
  <div class="abs report-title">TAXATION ESTIMATE FOR THE PERIOD ENDED</div>
  <div class="abs report-date">30 JUNE 2019</div>
  <div class="abs cover-footer">
    Bramwell Pty Ltd ACN 200 118 406 24 Ferndale Road, Riverton, WA 6148 PO Box 2210, Riverton, WA 6148<br>
    Tel: 08 7000 4120 Fax: 08 7000 4121 Email: info@harlowreed.com.au Director Daniel Harlow B Bus CA
  </div>
</section>

<section class="page left-page" aria-label="Disclaimer page">
  <span class="brand-dot" style="left:32px;top:19px;width:15px;height:15px"></span>
  <div class="run-rule" style="left:53px;top:23px;width:182px"></div>
  <div class="run-title" style="right:22px;top:17px">2019 TAX PLANNING | Northgate Plant Hire Pty Ltd</div>
  <div class="abs accent-bar"></div>
  <div class="abs disclaimer">
    <h2>DISCLAIMER</h2>
    <p>The taxation estimate has been prepared on the basis of information provided by the client. The report is intended for internal tax planning purposes and represents a "What if scenario". It does not necessarily represent real or intended transactions.</p>
    <p>HarlowReed have not performed any tests to verify or validate any of the information provided by the client and accordingly express no assurance as to the outcome indicated.</p>
    <p>To the extent permitted by law we do not accept liability for any loss or damage which any person, other than the client may suffer arising from any negligence on our part. No person should rely on the Taxation estimate without having a full review or audit conducted on the data.</p>
    <h3>Superannuation</h3>
    <p>Provision of Advice is guided by legislative requirements to be provided in a Statement of Advice. Any and all comments regarding Superannuation are not to be taken as advice rather than statement of factual information about the situation. The statement is not a recommendation to take any action unless that action is required by law. The clients personal situation has not been considered in providing the information. Any action to be taken in relation to the information provided, should take into account the clients personal situation and consideration must be given as to whether action will be appropriate for the clients' objectives and needs. Specific Contribution amounts and SMSF product advice can only be provided under a Statement of Advice by a AFSL Holder.</p>
    <div class="sign-off">Harlow Reed<br>Chartered Accountants</div>
  </div>
  <div class="page-no" style="left:22px">Page | 2</div>
</section>

<section class="page right-page" aria-label="Spreadsheet insert page">
  <div class="run-title" style="left:27px;top:17px">2019 TAX PLANNING | Northgate Plant Hire Pty Ltd</div>
  <div class="run-rule" style="left:27px;top:23px;width:183px"></div>
  <span class="brand-dot" style="left:214px;top:17px;width:15px;height:15px"></span>
  <div class="abs insert-label">Spreadsheet</div>
  <div class="page-no" style="left:210px">Page | 3</div>
</section>

<section class="page action-left" aria-label="Action plan page">
  <span class="brand-dot" style="left:32px;top:19px;width:15px;height:15px"></span>
  <div class="run-rule" style="left:52px;top:23px;width:182px"></div>
  <div class="run-title" style="right:23px;top:17px">2019 TAX PLANNING | Northgate Plant Hire Pty Ltd</div>
  <div class="action-heading" style="top:42px">Action Items to do now</div>
  <ul class="action-list">
    <li>Lorem ipsum</li><li>Lorem ipsum</li><li>Lorem ipsum</li>
    <li>Lorem ipsum</li><li>Lorem ipsum</li><li>Lorem ipsum</li>
  </ul>
  <div class="action-heading" style="top:122px">Action items to see others About</div>
  <div class="action-heading" style="top:202px">Action items for after year end</div>
  <div class="page-no" style="left:22px">Page | 4</div>
</section>

<section class="page action-right" aria-label="Tax planning strategies page">
  <div class="run-title" style="left:28px;top:17px">2019 TAX PLANNING | Northgate Plant Hire Pty Ltd</div>
  <div class="run-rule" style="left:28px;top:23px;width:181px"></div>
  <span class="brand-dot" style="left:216px;top:16px;width:15px;height:15px"></span>
  <div class="abs title-panel"></div>
  <div class="abs strategies-title">TAX PLANNING STRATEGIES</div>
  <div class="abs strategies-intro">A more detailed list of potential tax planning strategies is as follows:</div>
  <div class="abs main-heading">MAIN TAX PLANNING STRATEGIES</div>
  <div class="abs strategy-label">STRATEGY</div>
  <div class="abs strategies">
    <div class="strategy s1">
      <h4>Bring Forward Expenses</h4>
      <p>If possible, you should incur any business use expenses prior to 30 June. This way that expense will be included in the current tax year rather than NEXT tax year, reducing your tax payable in this financial year.</p>
      <p>Examples include: consumables, repairs, computer and office supplies.</p>
    </div>
    <div class="strategy s1">
      <h4>Defer Income</h4>
      <p>If possible, you should defer issuing invoices in the last week or two until after 30 June 2019. This way that income will be included in the 2020 tax year rather than the 2019 tax year, deferring tax on the income for a year. Cash basis taxpayers should defer receipt of payment if possible.</p>
    </div>
    <div class="strategy">
      <h4>Accounts Receivable</h4>
      <p>Under the small business tax concessions, the financial statements can be prepared on a cash basis so amounts receivable can be removed from the financial statements for tax purposes</p>
    </div>
    <div class="strategy">
      <h4>Accounts Payable</h4>
      <p>Under the small business tax concessions, the financial statements can be prepared on a cash basis so amounts payable can be removed from the financial statements for tax purposes</p>
    </div>
    <div class="strategy">
      <h4>Depreciation From Purchased Assets that Cost more than $30,000</h4>
      <p>A small business entity that purchases depreciating assets that cost more than:</p>
      <ul class="dash">
        <li>$30,000 from 3 April 2019 - 30 June 2019</li>
        <li>$25,000 from 29 January 2019 – 2 April 2019</li>
        <li>$20,000 from 1 July 2018 – 28 January 2019</li>
      </ul>
      <p>Will receive the following tax deductions from pooling the asset(s) in a small business asset pool:</p>
      <ul class="dot">
        <li>A 15% deduction in the 2019 tax year, regardless of when you purchased or acquired the asset during the year, and</li>
        <li>A 30% deduction each year after the first year.</li>
      </ul>
    </div>
    <div class="strategy">
      <h4>Bucket Company</h4>
      <p>If your business is trading through a trust and you have incurred higher than normal profits or the profits earned in your business are taxed at the highest marginal tax rate then a further tax planning strategy to consider is to set up a bucket company.</p>
    </div>
  </div>
  <div class="page-no" style="left:211px">Page | 5</div>
</section>

<section class="page back-cover" aria-label="Back cover">
  <span class="brand-dot" style="left:106px;top:227px;width:56px;height:56px"></span>
  <div class="abs" style="left:77px;top:293px">
    <div class="brand-name" style="font-size:11.5px">HARLOW REED</div>
    <div class="brand-tag">CHARTERED ACCOUNTANTS</div>
  </div>
  <div class="abs back-band"></div>
</section>

</body>
</html>
```